web site update

I want to get a better website for a small high end remodeling and construction company
I currently have a web site but you will find that it is not good.
www.quenbrickhall.com
We are a high end construction / remodeling company that has been in business since 2003. We primarily work in the mid peninsula of the bay area. Most of our clientele are very educated captains of industry. This group is still the target client.
I had my logo designed by Mint Easel a few years ago and I do like it, I like the orange and black or orange a blue. I don’t have a lot of content on hand as far as professional photographs.
Number of pages not sure and are open to: design pages vs full function website
I think what I am after is a web presence that will seal the deal as we are getting high referrals from past clients.
Construction
1 page

```html
<!DOCTYPE html>
<html lang="en">
<head>
<meta charset="utf-8">
<title>Quenbrick Hall Remodeling</title>
<link rel="stylesheet" href="https://fonts.googleapis.com/css2?family=Montserrat:wght@400;600;700&family=Roboto:wght@300;400;500;700&display=swap">
<style>
:root{
  --orange:#f47a2a;
  --orange-soft:#f79a5a;
  --ink:#1c1c1c;
  --text:#3a3a3a;
  --muted:#8a8a8a;
  --line:#dedede;
  --grey-btn:#7f7f7f;
  --white:#ffffff;
  --green:#3e9a3a;
}
*{box-sizing:border-box;margin:0;padding:0}
html,body{width:1200px;height:3681px;overflow:hidden}
body{font-family:"Roboto",Arial,sans-serif;color:var(--text);background:var(--white);position:relative}
.wrap{position:absolute;left:98px;width:1006px}

/* top bar */
.topbar{position:absolute;top:0;left:0;width:1200px;height:44px;border-bottom:1px solid var(--line)}
.topbar .social{position:absolute;left:98px;top:10px;display:flex;gap:10px}
.topbar .social span{width:20px;height:20px;background:#b5b5b5;border-radius:3px}
.topbar .util{position:absolute;right:96px;top:0;height:44px;display:flex;font-size:13px;color:var(--muted)}
.topbar .util div{display:flex;align-items:center;gap:8px;padding:0 22px;border-left:1px solid var(--line)}
.topbar .util div:last-child{border-right:1px solid var(--line)}

/* header */
.header{position:absolute;top:44px;left:0;width:1200px;height:91px}
.brand{position:absolute;left:98px;top:14px;display:flex;align-items:center;gap:14px}
.brand .mark{width:62px;height:62px;background:var(--orange)}
.brand .name{font-family:"Montserrat",sans-serif;font-weight:700;font-size:24px;color:var(--ink);line-height:1.1;letter-spacing:1px}
.nav{position:absolute;right:96px;top:32px;display:flex;gap:44px;font-family:"Montserrat",sans-serif;font-size:14px;font-weight:600;letter-spacing:1.5px;color:#8c8c8c}
.nav .active{color:var(--orange);border-bottom:3px solid var(--orange);padding-bottom:10px}

/* hero */
.hero{position:absolute;top:135px;left:0;width:1200px;height:597px;
  background:
    radial-gradient(ellipse 420px 360px at 78% 45%,rgba(150,120,95,.55),rgba(150,120,95,0) 70%),
    radial-gradient(ellipse 520px 300px at 18% 30%,rgba(205,200,190,.45),rgba(205,200,190,0) 70%),
    linear-gradient(180deg,#5e5852 0%,#3f3a35 60%,#2b2724 100%)}
.hero-text{position:absolute;left:160px;top:215px;width:880px;color:var(--white)}
.hero h1{font-family:"Montserrat",sans-serif;font-weight:600;font-size:41px;letter-spacing:1px;white-space:nowrap}
.hero h1 span{color:var(--orange)}
.hero .lead{font-family:"Montserrat",sans-serif;font-weight:700;font-size:18px;margin-top:8px;white-space:nowrap}
.hero .sub{font-family:"Montserrat",sans-serif;font-size:16px;line-height:1.5;margin-top:6px}

/* about */
.about{top:795px}
.about .rule{width:392px;height:2px;background:var(--orange)}
.about h2{font-family:"Montserrat",sans-serif;font-weight:400;font-size:25px;letter-spacing:4px;color:var(--orange);margin-top:18px}
.about h2 b{color:var(--ink);font-weight:700}
.about .intro{font-weight:700;font-size:16px;color:var(--ink);letter-spacing:1px;margin-top:32px}
.about p.body{font-size:13.5px;line-height:1.6;letter-spacing:1px;margin-top:20px;width:880px}

/* services */
.services{position:absolute;top:1026px;left:0;width:1200px;height:582px;
  background:
    radial-gradient(ellipse 300px 420px at 38% 40%,rgba(200,95,30,.35),rgba(200,95,30,0) 70%),
    radial-gradient(ellipse 300px 420px at 85% 50%,rgba(200,95,30,.3),rgba(200,95,30,0) 70%),
    linear-gradient(180deg,var(--orange-soft),var(--orange))}
.services .rule{position:absolute;left:98px;top:58px;width:392px;height:2px;background:#fff}
.services h2{position:absolute;left:98px;top:103px;font-family:"Montserrat",sans-serif;font-weight:600;font-size:27px;letter-spacing:4px;color:#fff}
.service{position:absolute;top:156px;width:200px;text-align:center;color:#fff}
.service .ring{width:148px;height:148px;margin:0 auto;border:5px solid #fff;border-radius:50%;display:flex;align-items:center;justify-content:center}
.service h3{font-family:"Montserrat",sans-serif;font-weight:600;font-size:16px;letter-spacing:3px;margin-top:52px}
.service p{font-size:11px;line-height:1.75;letter-spacing:1.5px;text-transform:uppercase;margin:22px auto 0;width:152px;color:#fde6d6}

/* gallery */
.gallery-head{position:absolute;top:1676px;left:0;width:1200px;text-align:center}
.gallery-head h2{font-family:"Montserrat",sans-serif;font-weight:700;font-size:24px;letter-spacing:2px;color:var(--orange)}
.gallery-head p{font-size:17px;color:var(--ink);margin-top:46px}
.filters{display:flex;justify-content:center;gap:4px;margin-top:52px}
.filters span{width:106px;height:45px;line-height:45px;background:var(--grey-btn);color:#fff;font-size:13px;font-weight:500}
.filters .on{background:var(--orange)}
.grid{position:absolute;top:1956px;left:0;width:1200px;height:478px;display:grid;grid-template-columns:repeat(4,1fr);grid-template-rows:repeat(2,1fr)}
.grid div:nth-child(1){background:radial-gradient(ellipse at 35% 40%,#e0b27e,#b9804c 55%,#8d5a31)}
.grid div:nth-child(2){background:radial-gradient(ellipse at 50% 70%,#c99567,#7a4526 55%,#3e2215)}
.grid div:nth-child(3){background:radial-gradient(ellipse at 50% 55%,#e6d8c2,#b59f82 55%,#7e6b55)}
.grid div:nth-child(4){background:radial-gradient(ellipse at 60% 50%,#d9cdb6,#a59a86 55%,#6b6152)}
.grid div:nth-child(5){background:radial-gradient(ellipse at 40% 40%,#c9b59a,#7d6a55 55%,#3f342a)}
.grid div:nth-child(6){background:radial-gradient(ellipse at 50% 45%,#d8c6b2,#8e99a6 55%,#4d5866)}
.grid div:nth-child(7){background:radial-gradient(ellipse at 60% 55%,#ece2d2,#a68d72 55%,#4e3c2d)}
.grid div:nth-child(8){background:radial-gradient(ellipse at 50% 40%,#e6d6bc,#a98d6b 55%,#4e3f31)}

/* cta */
.cta{position:absolute;top:2434px;left:0;width:1200px;height:151px;background:var(--orange-soft)}
.cta p{position:absolute;left:98px;top:36px;width:740px;padding-left:30px;border-left:4px solid #fff;color:#fff;font-weight:500;font-size:14px;line-height:1.65}
.cta .btn{position:absolute;left:963px;top:52px;width:138px;height:50px;border:2px solid #fff;background:#fff;color:var(--orange);font-weight:700;font-size:14px;text-align:center;line-height:46px;letter-spacing:1px}

/* team */
.portrait{position:absolute;left:98px;top:2667px;width:368px;height:368px;border-radius:50%;
  background:radial-gradient(ellipse 130px 150px at 52% 38%,#b9b9b9,#6e6e6e 60%,#2a2a2a 100%);
  box-shadow:0 6px 10px rgba(0,0,0,.35)}
.team{position:absolute;left:523px;top:2676px;width:581px}
.team h2{font-family:"Montserrat",sans-serif;font-weight:400;font-size:26px;color:var(--ink)}
.team h2 span{color:var(--orange);font-weight:700}
.team .rule{width:135px;height:3px;background:var(--orange);margin-top:18px}
.team h4{font-weight:700;font-size:14px;color:var(--ink);letter-spacing:.5px;margin-top:32px}
.team .role{font-size:14px;margin-top:8px}
.team .bio{font-size:14px;line-height:1.75;letter-spacing:1px;margin-top:38px;text-align:justify}
.team .mail{font-size:12.5px;line-height:1.5;margin-top:22px}
.team .more{display:inline-block;margin-top:16px;width:84px;height:38px;line-height:38px;text-align:center;background:var(--orange);color:#fff;font-size:12px;font-weight:500}

/* footer */
.footer{position:absolute;top:3141px;left:0;width:1200px;height:540px;
  background:
    radial-gradient(ellipse 500px 300px at 70% 30%,rgba(210,190,160,.45),rgba(210,190,160,0) 70%),
    linear-gradient(180deg,#f1ece5,#e7ddd0)}
.find{position:absolute;left:98px;top:60px;width:360px}
.find h3,.contact h3{font-family:"Montserrat",sans-serif;font-weight:400;font-size:24px;color:var(--ink)}
.contact h3 span{color:var(--orange);font-weight:700}
.find .intro{font-size:16px;line-height:1.4;margin-top:20px;color:var(--ink)}
.info{display:flex;gap:50px;margin-top:30px}
.info .dot{width:50px;height:50px;border-radius:50%;background:var(--orange);flex:none;display:flex;align-items:center;justify-content:center}
.info h5{font-size:13px;font-weight:700;color:var(--ink);margin-top:2px}
.info p{font-size:12.5px;line-height:1.45;margin-top:4px}
.contact{position:absolute;left:515px;top:60px;width:584px}
.contact form{margin-top:22px;display:grid;grid-template-columns:278px 278px;gap:14px 28px}
.contact .field{height:42px;background:#fff;border:1px solid #e2e2e2;font-size:12px;color:#9a9a9a;padding:12px 14px}
.contact .wide{grid-column:1/3}
.contact .msg{height:104px}
.contact .submit{grid-column:2;justify-self:end;width:118px;height:40px;background:var(--green);color:#fff;font-size:12px;font-weight:700;text-align:center;line-height:40px;letter-spacing:1px}
.footer .social{position:absolute;left:527px;top:445px;display:flex;gap:6px}
.footer .social span{width:32px;height:32px;background:#3b5a9a;border-radius:2px}
.footer .social span:nth-child(2){background:#4aa3df}
.footer .social span:nth-child(3){background:#2a72b0}
.footer .social span:nth-child(4){background:#d6492f}
</style>
</head>
<body>

<div class="topbar">
  <div class="social"><span></span><span></span><span></span><span></span><span></span></div>
  <div class="util">
    <div>
      <svg width="14" height="14" viewBox="0 0 24 24"><path d="M6 2h4l2 5-3 2a12 12 0 0 0 6 6l2-3 5 2v4a2 2 0 0 1-2 2A18 18 0 0 1 4 4a2 2 0 0 1 2-2z" fill="#9a9a9a"/></svg>555.204.7731
    </div>
    <div>
      <svg width="14" height="14" viewBox="0 0 24 24"><path d="M3 21l3-1 13-13-2-2L4 18z" fill="#9a9a9a"/></svg>Register
    </div>
    <div>
      <svg width="14" height="14" viewBox="0 0 24 24"><path d="M10 4h9v16h-9M3 12h11M10 8l4 4-4 4" fill="none" stroke="#9a9a9a" stroke-width="2"/></svg>Login
    </div>
  </div>
</div>

<header class="header">
  <div class="brand"><span class="mark"></span><span class="name">QUENBRICK<br>HALL</span></div>
  <nav class="nav">
    <span class="active">HOME</span><span>ABOUT US</span><span>SERVICES</span><span>GALLERY</span><span>CONTACT US</span>
  </nav>
</header>

<section class="hero" role="img" aria-label="Couple embracing in a living room overlaid with a sketched remodeling plan">
  <div class="hero-text">
    <h1>HOME IMPROVEMENT <span>IDEAS FOR YOU</span></h1>
    <p class="lead">LOREM IPSUM IS SIMPLY DUMMY TEXT OF THE PRINTING AND TYPESETTING INDUSTRY.</p>
    <p class="sub">LOREM IPSUM HAS BEEN THE INDUSTRY'S STANDARD DUMMY TEXT EVER SINCE THE 1500S, WHEN AN UNKNOWN PRINTER TOOK A GALLEY OF TYPE AND SCRAMBLED IT TO MAKE A TYPE SPECIMEN BOOK.</p>
  </div>
</section>

<section class="wrap about">
  <div class="rule"></div>
  <h2>About <b>Quenbrick Hall</b></h2>
  <p class="intro">Lorem Ipsum is simply dummy text of the printing and typesetting industry.</p>
  <p class="body">Lorem Ipsum has been the industry's standard dummy text ever since the 1500s, when an unknown printer took a galley of type and scrambled it to make a type specimen book. It has survived not only five centuries, but also the leap into electronic typesetting.</p>
</section>

<section class="services" role="img" aria-label="Painters decorating a wall, washed in orange">
  <div class="rule"></div>
  <h2>Remodeling Services</h2>

  <div class="service" style="left:72px">
    <div class="ring"><svg width="80" height="60" viewBox="0 0 80 60" fill="none" stroke="#fff" stroke-width="4"><rect x="6" y="8" width="68" height="18" rx="4"/><rect x="4" y="26" width="72" height="18" rx="3"/><path d="M8 44v10M72 44v10"/></svg></div>
    <h3>BEDROOMS</h3>
    <p>Fusce euismod consequat ante. Lorem ipsum dolor sit amet, consectetuer adipiscing elit.</p>
  </div>
  <div class="service" style="left:285px">
    <div class="ring"><svg width="84" height="60" viewBox="0 0 84 60" fill="none" stroke="#fff" stroke-width="4"><path d="M22 22h40M30 22v34M54 22v34M6 8v48M6 34h14v22M78 8v48M78 34H64v22"/></svg></div>
    <h3>DININGS</h3>
    <p>Fusce euismod consequat ante. Lorem ipsum dolor sit amet, consectetuer adipiscing elit.</p>
  </div>
  <div class="service" style="left:499px">
    <div class="ring"><svg width="80" height="64" viewBox="0 0 80 64" fill="none" stroke="#fff" stroke-width="4"><path d="M16 30V10a6 6 0 0 1 12 0M6 30h68M10 30v10a14 14 0 0 0 14 14h32a14 14 0 0 0 14-14V30M20 54l-4 8M60 54l4 8"/></svg></div>
    <h3>BATH ROOMS</h3>
    <p>Fusce euismod consequat ante. Lorem ipsum dolor sit amet, consectetuer adipiscing elit.</p>
  </div>
  <div class="service" style="left:712px">
    <div class="ring"><svg width="86" height="60" viewBox="0 0 86 60" fill="none" stroke="#fff" stroke-width="4"><path d="M16 24V12a6 6 0 0 1 6-6h42a6 6 0 0 1 6 6v12M4 28a6 6 0 0 1 12 0v10h54V28a6 6 0 0 1 12 0v18H4zM10 46v8M76 46v8"/></svg></div>
    <h3>DRAWING ROOM</h3>
    <p>Fusce euismod consequat ante. Lorem ipsum dolor sit amet, consectetuer adipiscing elit.</p>
  </div>
  <div class="service" style="left:926px">
    <div class="ring"><svg width="80" height="64" viewBox="0 0 80 64" fill="#fff"><rect x="8" y="4" width="28" height="14"/><rect x="44" y="4" width="28" height="14"/><rect x="4" y="30" width="72" height="4"/><rect x="6" y="36" width="20" height="24"/><rect x="30" y="36" width="20" height="24"/><rect x="54" y="36" width="20" height="24"/></svg></div>
    <h3>KITCHENS</h3>
    <p>Fusce euismod consequat ante. Lorem ipsum dolor sit amet, consectetuer adipiscing elit.</p>
  </div>
</section>

<section class="gallery-head">
  <h2>GALLERY</h2>
  <p>Lorem Ipsum is simply dummy text of the printing and typesetting industry industry.</p>
  <div class="filters"><span class="on">All</span><span>Bed Room</span><span>Dining</span><span>Bath Room</span><span>Kitchen</span><span>Dining</span></div>
</section>

<section class="grid">
  <div role="img" aria-label="Wooden house frame model with tools"></div>
  <div role="img" aria-label="Remodeled kitchen with dark wood cabinets"></div>
  <div role="img" aria-label="Kitchen under renovation with workers"></div>
  <div role="img" aria-label="Blueprints with a pencil and tape measure"></div>
  <div role="img" aria-label="Open-plan living room interior"></div>
  <div role="img" aria-label="Couple reviewing plans with a contractor"></div>
  <div role="img" aria-label="Renovated bathroom with vanity"></div>
  <div role="img" aria-label="Kitchen with island and bar stools"></div>
</section>

<section class="cta">
  <p>Lorem Ipsum is simply dummy text of the printing and typesetting industry. Lorem Ipsum has been the industry's standard dummy text ever since the 1500s, when an unknown printer took a galley of type and scrambled it to make a type specimen book.</p>
  <span class="btn">QUOTE NOW</span>
</section>

<div class="portrait" role="img" aria-label="Black and white portrait of the general manager"></div>
<section class="team">
  <h2>OUR <span>TEAM</span></h2>
  <div class="rule"></div>
  <h4>MR. MARLOW</h4>
  <p class="role">General Manager</p>
  <p class="bio">Lorem Ipsum is simply dummy text of the printing and typesetting industry. Lorem Ipsum has been the industry's standard dummy text ever since the 1500s. Lorem Ipsum is simply dummy standard dummy text ever since the 1500s</p>
  <p class="mail">info@quenbrickhall.com<br>marlow@quenbrickhall.com</p>
  <span class="more">MORE</span>
</section>

<footer class="footer" role="img" aria-label="Faint photo of a house under construction">
  <div class="find">
    <h3>IT'S EASY TO FIND US</h3>
    <p class="intro">Lorem Ipsum is simply dummy text of the printing and typesetting industry.</p>
    <div class="info">
      <span class="dot"><svg width="22" height="26" viewBox="0 0 24 28"><path d="M12 2a9 9 0 0 1 9 9c0 7-9 15-9 15S3 18 3 11a9 9 0 0 1 9-9z" fill="none" stroke="#fff" stroke-width="2.5"/><circle cx="12" cy="11" r="3" fill="#fff"/></svg></span>
      <div><h5>ADDRESS</h5><p>Suite 14, Alder Court,<br>Linden Vale</p></div>
    </div>
    <div class="info">
      <span class="dot"><svg width="22" height="22" viewBox="0 0 24 24"><path d="M6 2h4l2 5-3 2a12 12 0 0 0 6 6l2-3 5 2v4a2 2 0 0 1-2 2A18 18 0 0 1 4 4a2 2 0 0 1 2-2z" fill="#fff"/></svg></span>
      <div><h5>PHONES</h5><p>+1 555 0142 880 , +1 555 0142 881</p></div>
    </div>
    <div class="info">
      <span class="dot"><svg width="24" height="18" viewBox="0 0 24 18"><rect x="1" y="1" width="22" height="16" fill="none" stroke="#fff" stroke-width="2.5"/><path d="M1 1l11 9 11-9" fill="none" stroke="#fff" stroke-width="2.5"/></svg></span>
      <div><h5>EMAIL</h5><p>hello@quenbrickmail.com</p></div>
    </div>
  </div>

  <div class="contact">
    <h3>CONTACT <span>US</span></h3>
    <form>
      <div class="field">Name</div>
      <div class="field">Email</div>
      <div class="field wide">Subject</div>
      <div class="field wide msg">Message...</div>
      <div class="submit">SUBMIT</div>
    </form>
  </div>

  <div class="social"><span></span><span></span><span></span><span></span></div>
</footer>

</body>
</html>
```